Professional Consulting Firm Business Card Design

We need a business card design for a new professional consulting firm that specializes in petroleum, health, and financial consulting. We need a design that is trendy but elegant, and one that would make a vantage 300 executive feel comfortable using our services. I have attached a logo that needs to be used in the design. I have also attached a photo of a card design that I like.

On the card we need a place for employee name, title, email address, fax number, phone number, mailing address, and website address.

Industry/Entity Type

Financial

Contact Information for Business Card

see attached

Font styles to use
Other font styles liked:
• Calibri or your choice

Requirements
Must have
• style
Nice to have
• texture, rounded edges
Should not have
• no solid black cards but black may be used

```html
<!DOCTYPE html>
<html lang="en">
<head>
<meta charset="utf-8">
<title>Kestrel Consulting – Business Card</title>
<link rel="stylesheet" href="https://fonts.googleapis.com/css2?family=Didact+Gothic&family=Montserrat:wght@700&display=swap">
<style>
  :root {
    --backdrop: #1e1e1f;
    --card-white: #f4f4f2;
    --card-navy: #0f3a64;
    --navy: #163a66;
    --brand-blue: #1f4f80;
    --ink: #3a3a3a;
    --muted: #4a4a4a;
    --white: #ffffff;
  }
  * { margin: 0; padding: 0; box-sizing: border-box; }
  html, body {
    width: 1200px;
    height: 1000px;
    overflow: hidden;
    background: var(--backdrop);
  }
  .canvas {
    position: relative;
    width: 1200px;
    height: 1000px;
  }
  .card {
    position: absolute;
    width: 558px;
    height: 318px;
  }
  .card--front {
    left: 230px;
    top: 157px;
    background: var(--card-white);
  }
  .card--back {
    left: 418px;
    top: 520px;
    background: var(--card-navy);
  }
  .brand {
    position: absolute;
    display: flex;
    flex-direction: column;
    gap: 6px;
  }
  .card--front .brand { left: 36px; top: 56px; }
  .card--back .brand { left: 92px; top: 128px; }
  .brand__row {
    display: flex;
    align-items: center;
    gap: 12px;
  }
  .brand__square {
    width: 22px;
    height: 22px;
  }
  .brand__name {
    font-family: "Didact Gothic", sans-serif;
    font-size: 30px;
    line-height: 1;
    letter-spacing: 0.5px;
  }
  .brand__tagline {
    font-family: "Montserrat", sans-serif;
    font-weight: 700;
    font-size: 7px;
    letter-spacing: 0.2px;
    padding-left: 34px;
  }
  .card--front .brand__square { background: var(--brand-blue); }
  .card--front .brand__name,
  .card--front .brand__tagline { color: var(--brand-blue); }
  .card--back .brand__square { background: var(--white); }
  .card--back .brand__name,
  .card--back .brand__tagline { color: var(--white); }

  .address, .contacts {
    position: absolute;
    left: 36px;
    font-family: "Didact Gothic", sans-serif;
    font-size: 13.5px;
    line-height: 16.5px;
    color: var(--ink);
    list-style: none;
  }
  .address { top: 181px; }
  .contacts { top: 229px; }
  .contacts__label {
    font-family: "Montserrat", sans-serif;
    font-weight: 700;
    font-size: 12px;
    color: var(--navy);
  }
  .person {
    position: absolute;
    right: 36px;
    top: 229px;
    text-align: right;
  }
  .person__name {
    font-family: "Montserrat", sans-serif;
    font-weight: 700;
    font-size: 17px;
    letter-spacing: 0.6px;
    color: var(--navy);
  }
  .person__title {
    font-family: "Didact Gothic", sans-serif;
    font-size: 14.5px;
    color: var(--muted);
    margin-top: 2px;
  }
</style>
</head>
<body>
<main class="canvas">
  <section class="card card--front" aria-label="Business card front">
    <div class="brand">
      <div class="brand__row">
        <span class="brand__square"></span>
        <span class="brand__name">KESTREL CONSULTING LLC</span>
      </div>
      <span class="brand__tagline">HEALTH, SAFETY, AND FINANCIAL CONSULTING SERVICES</span>
    </div>

    <address class="address">
      218 W Palo Verde DR<br>
      Tucson,&nbsp; AZ&nbsp; 85710
    </address>

    <ul class="contacts">
      <li><span class="contacts__label">T:</span> (520) 555-0142</li>
      <li><span class="contacts__label">F:</span> (520) 555-0143</li>
      <li><span class="contacts__label">E:</span> jordan@kestrelco.com</li>
      <li><span class="contacts__label">W:</span> www.kestrelco.com</li>
    </ul>

    <div class="person">
      <p class="person__name">JORDAN ELLERY</p>
      <p class="person__title">General Manager</p>
    </div>
  </section>

  <section class="card card--back" aria-label="Business card back">
    <div class="brand">
      <div class="brand__row">
        <span class="brand__square"></span>
        <span class="brand__name">KESTREL CONSULTING LLC</span>
      </div>
      <span class="brand__tagline">HEALTH, SAFETY, AND FINANCIAL CONSULTING SERVICES</span>
    </div>
  </section>
</main>
</body>
</html>
```